Vehicle Signage

Please design a graphic layout for a Van signage to advertise the business

"Kestrel Alarm Works"
the logo is in the attached files

Also attached are some icons that represent the fields of service, I would like to use these in the design please
Updates

Reason: I am making some changes to the KAW logo to help match the Vans, I will up load the new files as soon as possible

Target Market(s)

We are targeting people who feel they would like to have some security equipment installed for piece of mind in the the fields of:
"Alarms, Intercoms, CCTV, Access Control"

Industry/Entity Type

Business

Requirements
Must have
• Must be Clear what we do,
it can be icons/pictures or words to represent the service areas of:

```html
<!DOCTYPE html>
<html lang="en">
<head>
<meta charset="utf-8">
<title>Kestrel Alarm Works – Van Side Signage</title>
<link rel="stylesheet" href="https://fonts.googleapis.com/css2?family=Russo+One&family=Signika:ital,wght@0,600;1,700&display=swap">
<style>
  :root {
    --green: #2bb45a;
    --lime: #b8d62a;
    --yellow: #e6ea3a;
    --charcoal: #3a3a3a;
    --navy: #1d3f5e;
    --panel: #ffffff;
    --page: #f2f2f2;
  }
  * { box-sizing: border-box; margin: 0; padding: 0; }
  html, body { width: 1200px; height: 970px; overflow: hidden; background: var(--page); }
  .canvas { position: relative; width: 1200px; height: 970px; }

  .service-icons { position: absolute; top: 10px; left: 0; width: 1200px; height: 160px; }
  .service-icon {
    position: absolute; top: 0; width: 170px; height: 160px; border-radius: 14px;
    background: linear-gradient(180deg, var(--green) 0%, var(--green) 62%, var(--charcoal) 62%, var(--charcoal) 100%);
  }
  .service-icon.alarms { left: 5px; }
  .service-icon.intercoms { left: 330px; }
  .service-icon.access { left: 620px; }
  .service-icon.cctv { left: 1025px; }

  .signage {
    position: absolute; left: 40px; top: 230px; width: 1120px; height: 700px;
    background: var(--panel); border-radius: 10px; overflow: hidden;
    box-shadow: 0 2px 10px rgba(0,0,0,.12);
  }
  .brand { position: absolute; left: 70px; top: 90px; display: flex; align-items: center; gap: 24px; }
  .brand-mark { width: 90px; height: 90px; border-radius: 50%; background: var(--navy); }
  .brand-name {
    font-family: "Russo One", sans-serif; font-size: 50px; line-height: 1.05;
    color: var(--navy); text-transform: uppercase; letter-spacing: 1px;
  }
  .phone {
    position: absolute; left: 180px; top: 270px;
    font-family: "Russo One", sans-serif; font-size: 84px; color: var(--green);
    -webkit-text-stroke: 3px var(--charcoal); letter-spacing: 3px;
  }
  .website {
    position: absolute; left: 60px; top: 380px;
    font-family: "Russo One", sans-serif; font-size: 70px; color: var(--charcoal);
    -webkit-text-stroke: 2px var(--green); letter-spacing: 2px;
  }
  .services { position: absolute; right: 50px; top: 60px; list-style: none; }
  .services li {
    display: flex; align-items: center; gap: 16px; height: 82px;
    font-family: "Signika", sans-serif; font-weight: 600; font-size: 36px; color: var(--charcoal);
  }
  .services li span::before { content: "• "; color: var(--green); }
  .service-chip {
    width: 52px; height: 52px; border-radius: 8px;
    background: linear-gradient(180deg, var(--green) 0%, var(--green) 60%, var(--charcoal) 60%, var(--charcoal) 100%);
  }

  .stripe-band {
    position: absolute; left: 0; bottom: 0; width: 1120px; height: 180px;
    background: linear-gradient(90deg, var(--yellow) 0%, var(--lime) 55%, var(--green) 100%);
  }
  .tagline {
    position: absolute; left: 500px; bottom: 118px;
    font-family: "Signika", sans-serif; font-style: italic; font-weight: 700;
    font-size: 40px; color: var(--charcoal);
  }
</style>
</head>
<body>
<div class="canvas">

  <div class="service-icons">
    <div class="service-icon alarms" role="img" aria-label="Alarm service icon"></div>
    <div class="service-icon intercoms" role="img" aria-label="Intercom service icon"></div>
    <div class="service-icon access" role="img" aria-label="Access control service icon"></div>
    <div class="service-icon cctv" role="img" aria-label="CCTV service icon"></div>
  </div>

  <section class="signage" aria-label="Van side panel">
    <div class="brand">
      <div class="brand-mark"></div>
      <div class="brand-name">Kestrel<br>Alarm Works</div>
    </div>

    <ul class="services">
      <li><div class="service-chip" role="img" aria-label="Alarm icon"></div><span>Alarms</span></li>
      <li><div class="service-chip" role="img" aria-label="Intercom icon"></div><span>Intercoms</span></li>
      <li><div class="service-chip" role="img" aria-label="Access control icon"></div><span>Access Control</span></li>
      <li><div class="service-chip" role="img" aria-label="CCTV icon"></div><span>CCTV</span></li>
    </ul>

    <div class="phone">555-0142</div>
    <div class="website">www.kaw.au.com</div>

    <div class="stripe-band" role="img" aria-label="Yellow to green decorative band"></div>
    <div class="tagline">“for your piece of mind”</div>
  </section>

</div>
</body>
</html>
```